Brightnest Dwelling Stationery Design

Letterpaper, business cards, notebook, envelope A4 & A5

Target Market(s)

Business, accommodation, hotels, flexible housing

Font styles to use
Other font styles liked:
• Montserrat

Colors

Designer to choose only greyscale colors for use in the design.

Requirements
Must have
• Luxurious appearance
Keep it simple, just like the logo
Modern
Nice to have
• Tight Luxury Design
Should not have
• Illustrations
Decorative

```html
<!DOCTYPE html>
<html lang="en">
<head>
<meta charset="utf-8">
<title>Brightnest Dwelling Business Card</title>
<link href="https://fonts.googleapis.com/css2?family=Montserrat:wght@300;400;500;600&display=swap" rel="stylesheet">
<style>
  :root {
    --backdrop: #3a3a3a;
    --card: #121212;
    --silver: #d9d9d9;
    --silver-soft: #9c9c9c;
    --ghost: #1f1f1f;
  }
  * { margin: 0; padding: 0; box-sizing: border-box; }
  html, body { width: 1200px; height: 960px; overflow: hidden; }
  body {
    background: var(--backdrop);
    font-family: "Montserrat", sans-serif;
    display: flex;
    flex-direction: column;
    align-items: center;
    justify-content: center;
    gap: 50px;
  }
  .card {
    position: relative;
    width: 720px;
    height: 411px;
    background: var(--card);
    border-radius: 24px;
    overflow: hidden;
  }
  .brand-mark {
    display: block;
    border: 3px solid var(--silver);
  }
  .brand-name {
    color: var(--silver);
    font-weight: 500;
    text-transform: uppercase;
    letter-spacing: 0.08em;
    white-space: nowrap;
  }
  /* Front */
  .card-front {
    display: flex;
    flex-direction: column;
    align-items: center;
    justify-content: center;
    gap: 26px;
  }
  .card-front .brand-mark { width: 110px; height: 110px; }
  .card-front .brand-name { font-size: 34px; }
  /* Back */
  .back-watermark {
    position: absolute;
    right: -40px;
    top: 150px;
    width: 230px;
    height: 210px;
    border: 3px solid var(--ghost);
  }
  .back-brand {
    position: absolute;
    top: 40px;
    right: 42px;
    display: flex;
    flex-direction: column;
    align-items: center;
    gap: 12px;
  }
  .back-brand .brand-mark { width: 62px; height: 62px; }
  .back-brand .brand-name { font-size: 17px; }
  .holder {
    position: absolute;
    left: 56px;
    top: 150px;
  }
  .holder-name { color: var(--silver); font-weight: 600; font-size: 24px; line-height: 1.2; }
  .holder-role { color: var(--silver-soft); font-weight: 300; font-size: 17px; margin-top: 2px; }
  .contact {
    position: absolute;
    left: 56px;
    top: 232px;
    color: var(--silver);
    font-weight: 300;
    font-size: 16px;
    line-height: 1.3;
  }
  .address-label { font-weight: 600; }
  .contact-lines { margin-top: 10px; list-style: none; }
  .contact-lines li { display: flex; align-items: center; gap: 14px; height: 24px; }
  .contact-lines svg { width: 15px; height: 15px; fill: var(--silver); flex: none; }
</style>
</head>
<body>
  <section class="card card-front">
    <span class="brand-mark"></span>
    <span class="brand-name">Brightnest Dwelling</span>
  </section>

  <section class="card card-back">
    <span class="back-watermark"></span>
    <div class="back-brand">
      <span class="brand-mark"></span>
      <span class="brand-name">Brightnest Dwelling</span>
    </div>
    <div class="holder">
      <p class="holder-name">Dana Whitlow</p>
      <p class="holder-role">Founder</p>
    </div>
    <div class="contact">
      <p class="address-label">Address:</p>
      <p>48 Harbor lane suite 210</p>
      <p>Portland or 97201</p>
      <ul class="contact-lines">
        <li>
          <svg viewBox="0 0 16 16" aria-hidden="true"><path d="M3.5 1l2.5 3-1.5 1.8c.9 2 2.6 3.7 4.6 4.6L10.9 9l3 2.5-1.3 2.7C7 14 2 9 1.8 3.1z"/></svg>
          <span>0422581046</span>
        </li>
        <li>
          <svg viewBox="0 0 16 16" aria-hidden="true"><path d="M1 3h14v10H1z M2 4.2v.5l6 4 6-4v-.5z" fill-rule="evenodd"/></svg>
          <span>dana@brightnestdwelling.com</span>
        </li>
        <li>
          <svg viewBox="0 0 16 16" aria-hidden="true"><path d="M8 1a7 7 0 1 0 0 14A7 7 0 0 0 8 1zm-1 1.6V5H4.3A5.5 5.5 0 0 1 7 2.6zm2 0A5.5 5.5 0 0 1 11.7 5H9zM3.6 6.5H7v3H3.6zm5.4 0h3.4v3H9zM4.3 11H7v2.4A5.5 5.5 0 0 1 4.3 11zM9 11h2.7A5.5 5.5 0 0 1 9 13.4z"/></svg>
          <span>www.brightnestdwelling.com</span>
        </li>
      </ul>
    </div>
  </section>
</body>
</html>
```